Wine Label for a White and a Red Wine from Italy

We have a very good idea of what we want with artwork. We need you to please design a 'template' with the text so we can change out the artwork from year to year. Samples are shown of what we are looking for. We are looking for options with the two basic designs. Brand name of wine is: Valora del Torrino. Both wines are in a light green Bordeaux-style bottle (note: we don't show a light green bottle in the mockup but please remember the bottle is light green). Artwork is provided. We'd like to see either the green or blue butterfly on the white wine, the red butterfly is for the red wine. Please base the design on the attached label from Ashby and/or the attached label from Chateau Vellanges.

Target Market(s)

Millennials, women

Requirements
Must have
• The artwork (butterflies) attached.
Nice to have
• Elegant, readable fonts. Please make the text so it can be changed by the printer. Please make it so the artwork can be changed too.

```html
<!DOCTYPE html>
<html lang="it">
<head>
<meta charset="utf-8">
<title>Valora del Torrino – Barrel Select Labels</title>
<link rel="stylesheet" href="https://fonts.googleapis.com/css2?family=Old+Standard+TT:wght@400&display=swap">
<style>
  :root {
    --page-bg: #f5f5f5;
    --label-bg: #ffffff;
    --label-edge: #e4e4e4;
    --ink: #111111;
    --amber-light: #f7c843;
    --amber: #eea51c;
    --amber-deep: #c8790f;
    --teal: #1a8c8c;
    --crimson: #b32418;
    --frame: #222222;
  }
  * { margin: 0; padding: 0; box-sizing: border-box; }
  html, body {
    width: 1082px; height: 1200px; overflow: hidden;
    background: var(--page-bg);
  }
  .sheet {
    position: relative; width: 1082px; height: 1200px;
    font-family: "Old Standard TT", Georgia, serif;
    color: var(--ink);
  }
  .panel {
    position: absolute; left: 0; width: 1082px; height: 594px;
    border: 1px solid var(--frame);
    background: var(--page-bg);
  }
  .panel--top { top: 0; }
  .panel--bottom { top: 606px; }
  .label {
    position: absolute; top: 64px; width: 323px; height: 463px;
    background: linear-gradient(90deg, var(--label-edge) 0%, var(--label-bg) 14%, var(--label-bg) 84%, var(--label-edge) 100%);
    box-shadow: 0 1px 4px rgba(0,0,0,0.12);
  }
  .label--white { left: 144px; }
  .label--red { left: 631px; }
  .line {
    position: absolute; left: 0; right: 0; text-align: center;
    line-height: 1; transform: translateY(-50%); white-space: nowrap;
  }
  .brand-name { font-size: 40px; letter-spacing: 0.2em; padding-left: 0.2em; }
  .brand-region { font-size: 17px; }
  .range { font-size: 20px; letter-spacing: 0.01em; }
  .vintage { font-size: 15px; }
  .vintage--large { font-size: 22px; }
  .wine-type { font-size: 20px; }
  .origin { font-size: 14.5px; }
  .maker { font-size: 13.5px; }
  .artwork { position: absolute; border-radius: 10px 18px 8px 22px; }
  .artwork--teal {
    background: radial-gradient(ellipse at 50% 45%, var(--teal) 0%, #3f8f6a 28%, var(--amber) 52%, var(--amber-light) 75%, var(--amber-deep) 100%);
  }
  .artwork--red {
    background: radial-gradient(ellipse at 45% 60%, var(--crimson) 0%, #d2441b 26%, var(--amber) 55%, var(--amber-light) 85%);
    border-radius: 30px 24px 40px 50px;
  }
</style>
</head>
<body>
<div class="sheet">

  <section class="panel panel--top">
    <article class="label label--white">
      <div class="line brand-name" style="top:40px">VALORA</div>
      <div class="line brand-region" style="top:68px">del Torrino</div>
      <div class="artwork artwork--teal" role="img" aria-label="Teal butterfly painted over amber brush strokes" style="left:30px; top:79px; width:279px; height:232px"></div>
      <div class="line range" style="top:319px">BARREL SELECT</div>
      <div class="line vintage vintage--large" style="top:341px">2018</div>
      <div class="line wine-type" style="top:368px">Bianco</div>
      <div class="line origin" style="top:388px">Piemonte, Itely</div>
      <div class="line maker" style="top:419px">Artisanlly Crafted by Cantina Quattro Colli</div>
      <div class="line maker" style="top:438px">sustainably farmed</div>
    </article>

    <article class="label label--red">
      <div class="line brand-name" style="top:43px">VALORA</div>
      <div class="line brand-region" style="top:71px">del Torrino</div>
      <div class="artwork artwork--red" role="img" aria-label="Red butterfly painted over amber brush strokes" style="left:77px; top:80px; width:174px; height:213px"></div>
      <div class="line range" style="top:300px">BARREL SELECT</div>
      <div class="line vintage" style="top:330px">2018</div>
      <div class="line wine-type" style="top:356px">Rosso</div>
      <div class="line origin" style="top:376px">Piemonte, Itely</div>
      <div class="line maker" style="top:408px">Artisanlly Crafted by Cantina Quattro Colli</div>
      <div class="line maker" style="top:427px">sustainably farmed</div>
    </article>
  </section>

  <section class="panel panel--bottom">
    <article class="label label--white">
      <div class="line brand-name" style="top:48px">VALORA</div>
      <div class="line brand-region" style="top:76px">del Torrino</div>
      <div class="artwork artwork--teal" role="img" aria-label="Teal butterfly painted over amber brush strokes" style="left:57px; top:95px; width:210px; height:180px"></div>
      <div class="line range" style="top:300px">BARREL SELECT</div>
      <div class="line vintage" style="top:330px">2018</div>
      <div class="line wine-type" style="top:356px">Bianco</div>
      <div class="line origin" style="top:376px">Piemonte, Itely</div>
      <div class="line maker" style="top:408px">Artisanlly Crafted by Cantina Quattro Colli</div>
      <div class="line maker" style="top:427px">sustainably farmed</div>
    </article>

    <article class="label label--red">
      <div class="line brand-name" style="top:48px">VALORA</div>
      <div class="line brand-region" style="top:76px">del Torrino</div>
      <div class="artwork artwork--red" role="img" aria-label="Red butterfly painted over amber brush strokes" style="left:89px; top:91px; width:150px; height:190px"></div>
      <div class="line range" style="top:300px">BARREL SELECT</div>
      <div class="line vintage" style="top:330px">2018</div>
      <div class="line wine-type" style="top:356px">Rosso</div>
      <div class="line origin" style="top:376px">Piemonte, Itely</div>
      <div class="line maker" style="top:408px">Artisanlly Crafted by Cantina Quattro Colli</div>
      <div class="line maker" style="top:427px">sustainably farmed</div>
    </article>
  </section>

</div>
</body>
</html>
```